'TOLVANTA' NEW WINE LABEL DESIGN

I am looking for an exceptional and exciting design for a wine label called 'Tolvanta' meaning 'Lookout'. The design must feature the name 'Tolvanta', and the word 'Cabernet Sauvignon' in version 1 and 'Sauvignon Blanc' in version 2. It will also need the words 'Valle Central, Chile' at the bottom of the label as a prominent piece of information as well as the vintage 2017. Please produce the work in size 80mm x 100mm. Feel free to use colour in addition to black/white and ensue that the label is easy to read on a shelf placement.
Target Market(s)
SUPERMARKETS & WINE STORES
Requirements
Must have
- EASY TO READ, USE COLOURS LIKE GREEN FOR SAUVIGNON & RED FOR CABERNET SAUVIGNON
- FULL BOTTLE SHOT MUST BE IN PROVIDED DESIGNS. ALL BOTTLE TOPS SHOULD BE QUORLAN STYLE (SCREW TOP)
- PLEASE NOTE THAT LABEL INFORMATION MUSY BE EASY TO READ I.E. VINTAGE, PLACE OF ORGIN ALTHOUGH NOT THE MAIN CONTENT MUST STILL BE CLEAR.
Nice to have
- ARTISTIC REFERENCE LINK TO NAME & ANDES BUT NOT PICTURES OF MOUNTAINS
Should not have
- PICTURES OF GRAPES
- PICTURES OF VINEYARDS
- PICTURES OF MOUNTAINS

```html
<!DOCTYPE html>
<html lang="en">
<head>
<meta charset="utf-8">
<title>Tolvanta Wine Labels</title>
<link rel="stylesheet" href="https://fonts.googleapis.com/css2?family=Marcellus&family=Montserrat:wght@500&family=Pinyon+Script&display=swap">
<style>
  :root {
    --page-bg: #d8ddd4;
    --label-bg: #231f20;
    --pattern-tone: #2e2b2c;
    --text-light: #ffffff;
    --cabernet-red: #e8262b;
    --sauvignon-green: #9acd3c;
  }
  * { box-sizing: border-box; margin: 0; padding: 0; }
  html, body {
    width: 1200px;
    height: 1081px;
    overflow: hidden;
    background: var(--page-bg);
  }
  .label-sheet {
    position: relative;
    width: 1200px;
    height: 1081px;
    display: flex;
    justify-content: center;
    align-items: center;
    gap: 60px;
  }
  .wine-label {
    position: relative;
    width: 500px;
    height: 625px;
    background: var(--label-bg);
    overflow: hidden;
    text-align: center;
    color: var(--text-light);
  }
  .wine-label--cabernet { --accent: var(--cabernet-red); }
  .wine-label--sauvignon { --accent: var(--sauvignon-green); }

  .label-pattern {
    position: absolute;
    inset: 0;
    background: radial-gradient(ellipse 62% 60% at 50% 50%, var(--pattern-tone) 0%, var(--pattern-tone) 55%, var(--label-bg) 100%);
  }
  .brand-mark {
    position: absolute;
    left: 50%;
    top: 108px;
    width: 78px;
    height: 78px;
    margin-left: -39px;
    background: var(--accent);
  }
  .brand-name {
    position: absolute;
    left: 0;
    right: 0;
    top: 262px;
    font-family: "Marcellus", serif;
    font-size: 78px;
    line-height: 1;
    letter-spacing: 1px;
    color: var(--text-light);
  }
  .varietal {
    position: absolute;
    left: 0;
    right: 0;
    top: 358px;
    font-family: "Montserrat", sans-serif;
    font-weight: 500;
    font-size: 25px;
    letter-spacing: 3px;
    color: var(--accent);
  }
  .wine-label--sauvignon .varietal { letter-spacing: 5px; }
  .origin {
    position: absolute;
    left: 0;
    right: 0;
    top: 490px;
    font-family: "Pinyon Script", cursive;
    font-size: 38px;
    line-height: 1;
    color: var(--text-light);
  }
  .vintage {
    position: absolute;
    left: 0;
    right: 0;
    top: 544px;
    display: flex;
    justify-content: center;
    align-items: center;
    gap: 10px;
    font-family: "Montserrat", sans-serif;
    font-weight: 500;
    font-size: 23px;
    letter-spacing: 1px;
    color: var(--text-light);
  }
  .vintage-swash { width: 24px; height: 10px; }
  .vintage-swash path { fill: none; stroke: var(--accent); stroke-width: 3; stroke-linecap: round; }
</style>
</head>
<body>
<main class="label-sheet">
  <section class="wine-label wine-label--cabernet">
    <div class="label-pattern" role="img" aria-label="Faint interlocking geometric pattern behind the label text"></div>
    <div class="brand-mark"></div>
    <h1 class="brand-name">TOLVANTA</h1>
    <p class="varietal">CABERNET SAUVIGNON</p>
    <p class="origin">Valle Central, Chile</p>
    <p class="vintage">
      <svg class="vintage-swash" viewBox="0 0 24 10"><path d="M2 3 Q8 9 14 6 T22 4"/></svg>
      2017
      <svg class="vintage-swash" viewBox="0 0 24 10"><path d="M2 6 Q8 2 12 5 T22 3"/></svg>
    </p>
  </section>

  <section class="wine-label wine-label--sauvignon">
    <div class="label-pattern" role="img" aria-label="Faint interlocking geometric pattern behind the label text"></div>
    <div class="brand-mark"></div>
    <h1 class="brand-name">TOLVANTA</h1>
    <p class="varietal">SAUVIGNON BLANC</p>
    <p class="origin">Valle Central, Chile</p>
    <p class="vintage">
      <svg class="vintage-swash" viewBox="0 0 24 10"><path d="M2 3 Q8 9 14 6 T22 4"/></svg>
      2017
      <svg class="vintage-swash" viewBox="0 0 24 10"><path d="M2 6 Q8 2 12 5 T22 3"/></svg>
    </p>
  </section>
</main>
</body>
</html>
```